Business card for medical clinic

I need an upmarket, modern medical/health business card for my clinic

Contact Information for Business Card

name, address, email, qr code

```html
<!DOCTYPE html>
<html lang="en">
<head>
<meta charset="utf-8">
<title>Meridian Care Partners – Business Card</title>
<link rel="stylesheet" href="https://fonts.googleapis.com/css2?family=Montserrat:wght@400;500;600;700&display=swap">
<style>
  :root {
    --navy: #222f4a;
    --sky: #29abe2;
    --brand-blue: #2a6fa8;
    --white: #ffffff;
    --ink: #1d2333;
    --stage: #a5a6a8;
  }
  * { margin: 0; padding: 0; box-sizing: border-box; }
  html, body { width: 1200px; height: 900px; overflow: hidden; }
  body {
    background: var(--stage);
    font-family: "Montserrat", Arial, sans-serif;
    position: relative;
  }
  .card {
    position: absolute;
    left: 250px;
    width: 700px;
    height: 400px;
    border-radius: 22px;
    overflow: hidden;
  }
  .card-back { top: 30px; background: var(--navy); }
  .card-front { top: 470px; background: var(--white); }

  .brand {
    position: absolute;
    display: flex;
    align-items: center;
    gap: 18px;
  }
  .brand-dot {
    border-radius: 50%;
    border-style: solid;
    flex: none;
  }
  .brand-name {
    font-weight: 600;
    letter-spacing: 0.12em;
    text-transform: uppercase;
    white-space: nowrap;
  }
  .card-back .brand {
    left: 50%; top: 50%;
    transform: translate(-50%, -50%);
  }
  .card-back .brand-dot { width: 86px; height: 86px; border-width: 5px; border-color: var(--white); }
  .card-back .brand-name { color: var(--white); font-size: 30px; }

  .card-front .brand { left: 52px; top: 150px; gap: 12px; }
  .card-front .brand-dot { width: 48px; height: 48px; border-width: 3px; border-color: var(--navy); }
  .card-front .brand-name { color: var(--navy); font-size: 15px; }

  .divider {
    position: absolute;
    left: 395px; top: 86px;
    width: 1.5px; height: 160px;
    background: var(--sky);
  }
  .contact-block {
    position: absolute;
    left: 418px; top: 82px;
  }
  .person-name { font-size: 28px; font-weight: 700; color: var(--brand-blue); line-height: 1.1; }
  .person-title { font-size: 14px; font-weight: 500; color: var(--ink); margin-top: 4px; }
  .contact-list { list-style: none; margin-top: 24px; }
  .contact-list li {
    display: flex; align-items: center; gap: 12px;
    font-size: 14.5px; color: var(--ink); margin-bottom: 11px;
  }
  .contact-icon { width: 15px; height: 15px; flex: none; }

  .band { position: absolute; left: 0; bottom: 0; width: 700px; height: 90px; }
  .address {
    position: absolute;
    left: 170px; bottom: 17px;
    font-size: 15px; font-weight: 500;
    color: var(--white);
    letter-spacing: 0.01em;
    white-space: nowrap;
  }
</style>
</head>
<body>

  <section class="card card-back">
    <div class="brand">
      <span class="brand-dot"></span>
      <span class="brand-name">Meridian Care Partners</span>
    </div>
  </section>

  <section class="card card-front">
    <div class="brand">
      <span class="brand-dot"></span>
      <span class="brand-name">Meridian Care Partners</span>
    </div>

    <div class="divider"></div>

    <div class="contact-block">
      <p class="person-name">Daniel Harper</p>
      <p class="person-title">Managing Director</p>
      <ul class="contact-list">
        <li>
          <svg class="contact-icon" viewBox="0 0 16 16"><path fill="#29abe2" d="M3.6 1.5l2.3 2.6-1.3 1.6c.9 2 2.5 3.6 4.5 4.6l1.6-1.3 2.6 2.3-1.5 2.2C7 13.5 2.5 9 1.5 3.1z"/></svg>
          <span>555.210.4473</span>
        </li>
        <li>
          <svg class="contact-icon" viewBox="0 0 16 16"><rect x="1" y="3.5" width="14" height="9.5" rx="1" fill="#29abe2"/><path d="M1.5 4.2L8 9l6.5-4.8" stroke="#fff" stroke-width="1.2" fill="none"/></svg>
          <span>hello@meridiancare.com</span>
        </li>
        <li>
          <svg class="contact-icon" viewBox="0 0 16 16"><circle cx="8" cy="8" r="7" fill="#29abe2"/><path d="M1 8h14M8 1c-3 3.5-3 10.5 0 14M8 1c3 3.5 3 10.5 0 14" stroke="#fff" stroke-width="1" fill="none"/></svg>
          <span>www.meridiancare.com</span>
        </li>
      </ul>
    </div>

    <svg class="band" viewBox="0 0 700 90" aria-hidden="true">
      <polygon points="0,34 530,34 512,90 0,90" fill="#222f4a"/>
      <polygon points="548,0 700,0 700,58 532,58" fill="#29abe2"/>
    </svg>
    <p class="address">42 Cedar Brook Lane Ridgeford, MS 39020</p>
  </section>

</body>
</html>
```